Need wine label for brand that is named: Tolmesha Vineyards & Winery

Tolmesha is a yoga way of breathing. In Sanskrit Tolmesha means "flying up." I would like a creative wine label that articulates Tolmesha. The label should include a graphic and the name Tolmesha on one line and Vineyards & Winery in smaller print underneath Tolmesha.

```html
<!DOCTYPE html>
<html lang="en">
<head>
<meta charset="utf-8">
<title>Tolmesha Vineyards &amp; Winery – White Wine Label</title>
<link rel="stylesheet" href="https://fonts.googleapis.com/css2?family=Montserrat:wght@400;500;600;700&family=Yellowtail&display=swap">
<style>
  :root {
    --paper: #f4f3ef;
    --navy: #22304b;
    --teal: #5b939b;
    --feather-deep: #4f7f8c;
    --feather-mid: #8fb0b8;
    --feather-light: #c9d8d9;
  }
  * { margin: 0; padding: 0; box-sizing: border-box; }
  html, body {
    width: 739px;
    height: 1200px;
    overflow: hidden;
    background: var(--paper);
  }
  .label {
    position: relative;
    width: 739px;
    height: 1200px;
    background: var(--paper);
    font-family: "Montserrat", sans-serif;
    color: var(--navy);
    text-align: center;
    overflow: hidden;
  }
  .feather-canopy {
    position: absolute;
    left: 0;
    top: 0;
    width: 739px;
    height: 500px;
    background:
      radial-gradient(ellipse 120px 190px at 120px 220px, rgba(79,127,140,.55), transparent 70%),
      radial-gradient(ellipse 110px 200px at 380px 200px, rgba(79,127,140,.6), transparent 70%),
      radial-gradient(ellipse 100px 180px at 590px 160px, rgba(79,127,140,.55), transparent 70%),
      linear-gradient(180deg, rgba(143,176,184,.55) 0%, rgba(201,216,217,.35) 60%, rgba(244,243,239,0) 100%);
  }
  .feather-drift {
    position: absolute;
    border-radius: 50%;
    background: radial-gradient(ellipse at center, rgba(143,176,184,.55), rgba(201,216,217,0) 70%);
  }
  .feather-drift--a { left: 420px; top: 405px; width: 160px; height: 70px; transform: rotate(18deg); }
  .feather-drift--b { left: 70px;  top: 705px; width: 80px;  height: 170px; transform: rotate(-20deg); }
  .feather-drift--c { left: 625px; top: 705px; width: 120px; height: 60px;  transform: rotate(-25deg); }
  .feather-drift--d { left: 620px; top: 815px; width: 100px; height: 50px;  transform: rotate(25deg); }
  .feather-drift--e { left: 0;     top: 850px; width: 90px;  height: 110px; transform: rotate(40deg); }
  .feather-drift--f { left: 10px;  top: 1125px; width: 100px; height: 60px; transform: rotate(-30deg); }

  .brand-name {
    position: absolute;
    left: 0;
    right: 0;
    top: 500px;
    font-family: "Yellowtail", cursive;
    font-weight: 400;
    font-size: 128px;
    line-height: 1;
    color: var(--navy);
  }
  .brand-sub {
    position: absolute;
    left: 0; right: 0;
    top: 736px;
    font-size: 30px;
    font-weight: 700;
    letter-spacing: 1.5px;
    color: var(--teal);
  }
  .vintage {
    position: absolute;
    left: 0; right: 0;
    top: 797px;
    font-size: 20px;
    font-weight: 700;
    letter-spacing: 1.5px;
  }
  .wine-style {
    position: absolute;
    left: 0; right: 0;
    top: 832px;
    font-size: 21px;
    font-weight: 400;
    letter-spacing: 1.6px;
  }
  .producer {
    position: absolute;
    left: 0; right: 0;
    top: 883px;
    font-size: 16.5px;
    line-height: 22px;
    letter-spacing: 1.4px;
  }
  .allergen {
    position: absolute;
    left: 0; right: 0;
    top: 953px;
    font-size: 16px;
    font-weight: 600;
    letter-spacing: 1px;
    color: var(--teal);
  }
  .health-warning {
    position: absolute;
    left: 50px; right: 50px;
    top: 987px;
    font-size: 14px;
    line-height: 18.5px;
    letter-spacing: .6px;
    color: var(--teal);
  }
  .abv {
    position: absolute;
    left: 0; right: 0;
    top: 1076px;
    font-size: 17px;
    font-weight: 700;
    letter-spacing: 1px;
  }
</style>
</head>
<body>
  <main class="label">
    <div class="feather-canopy" role="img" aria-label="Watercolour illustration of blue-green feathers hanging down from the top edge"></div>
    <div class="feather-drift feather-drift--a" role="img" aria-label="Small watercolour feather drifting"></div>
    <div class="feather-drift feather-drift--b" role="img" aria-label="Small watercolour feather drifting"></div>
    <div class="feather-drift feather-drift--c" role="img" aria-label="Small watercolour feather drifting"></div>
    <div class="feather-drift feather-drift--d" role="img" aria-label="Small watercolour feather drifting"></div>
    <div class="feather-drift feather-drift--e" role="img" aria-label="Small watercolour feather drifting"></div>
    <div class="feather-drift feather-drift--f" role="img" aria-label="Small watercolour feather drifting"></div>

    <h1 class="brand-name">Tolmesha</h1>
    <p class="brand-sub">VINEYARDS &amp; WINERY</p>
    <p class="vintage">- 2017 -</p>
    <p class="wine-style">A LIGHT AND FRUITY WHITE WINE</p>
    <p class="producer">GROWN VINTED AND BOTTLED BY<br>TOLMESHA VINEYARDS &amp; WINERY</p>
    <p class="allergen">CONTAINS SULPHITES</p>
    <p class="health-warning">Government warning: (1) According to the surgeon general, women should not drink alcoholic beverages during pregnancy because of the risk of birth defects. (2) Consumption of alcoholic beverages impacts your ability to drive a car or operate machinery and may cause health problems.</p>
    <p class="abv">ALCOHOL 11.2% BY VOLUME</p>
  </main>
</body>
</html>
```